Business Card Design

We need a business card to highlight our property maintenance company. we specialize in commercial and industrial property maintenance. services include landscaping snow and ice management. janitorial services. cleanroom services. parking lot maintenance.
Updates
I have narrowed down to two designs thank you waiting on some minor changes to both designs to choose.
Target Market(s)
facility managers/property managers
Industry/Entity Type
Property Maintenance
Contact Information for Business Card
47 Brindlewood Rd.
Sterling, Ma. 01839
978-552-3716
Look and feel

```html
<!DOCTYPE html>
<html lang="en">
<head>
<meta charset="utf-8">
<title>Property Maintenance Business Card – Services</title>
<link rel="stylesheet" href="https://fonts.googleapis.com/css2?family=EB+Garamond:wght@700;800&display=swap">
<style>
  :root {
    --navy: #06065a;
    --gold: #f7c600;
    --white: #ffffff;
    --photo-dark: #55566f;
    --photo-mid: #8f91bd;
    --photo-light: #d9dbef;
    --shadow: rgba(10, 10, 30, 0.75);
  }
  html, body {
    margin: 0;
    padding: 0;
    width: 1200px;
    height: 702px;
    overflow: hidden;
    background: #ffffff;
  }
  .card {
    position: relative;
    width: 1200px;
    height: 702px;
    overflow: hidden;
    font-family: "EB Garamond", Georgia, serif;
    font-weight: 800;
  }
  .card__photo {
    position: absolute;
    left: 0;
    top: 0;
    width: 1200px;
    height: 583px;
    background:
      radial-gradient(ellipse 420px 260px at 1080px 120px, rgba(240,241,250,0.85), rgba(240,241,250,0) 70%),
      radial-gradient(ellipse 380px 220px at 150px 420px, rgba(200,202,230,0.55), rgba(200,202,230,0) 70%),
      linear-gradient(125deg, var(--photo-dark) 0%, #6f7194 30%, var(--photo-mid) 60%, var(--photo-light) 100%);
  }
  .card__band {
    position: absolute;
    left: 0;
    width: 1200px;
  }
  .card__band--navy-top { top: 583px; height: 58px; background: var(--navy); }
  .card__band--gold { top: 641px; height: 15px; background: var(--gold); }
  .card__band--navy-bottom { top: 656px; height: 46px; background: var(--navy); }

  .rule {
    position: absolute;
    left: 246px;
    width: 718px;
    height: 2px;
    background: var(--navy);
  }
  .rule--1 { top: 132px; }
  .rule--2 { top: 278px; }
  .rule--3 { top: 364px; }

  .heading, .specialty, .service {
    position: absolute;
    margin: 0;
    line-height: 1;
    text-shadow: 3px 3px 4px var(--shadow);
  }
  .heading {
    left: 0;
    width: 1212px;
    text-align: center;
    color: var(--gold);
    font-size: 56px;
  }
  .heading--specialize { top: 58px; }
  .heading--services { top: 296px; }

  .specialty {
    left: 0;
    width: 1212px;
    top: 148px;
    text-align: center;
    color: var(--white);
    font-size: 45px;
    line-height: 52px;
  }

  .services-list {
    position: absolute;
    margin: 0;
    padding: 0;
    list-style: none;
  }
  .services-list--left { left: 110px; top: 392px; }
  .services-list--right { left: 606px; top: 392px; }
  .service {
    position: relative;
    color: var(--white);
    font-size: 45px;
    line-height: 49px;
    white-space: nowrap;
  }
</style>
</head>
<body>
  <main class="card">
    <div class="card__photo" role="img" aria-label="Soft blue-tinted photograph of a gloved hand holding a cleaning tool"></div>

    <h2 class="heading heading--specialize">We specialize in</h2>
    <div class="rule rule--1"></div>
    <p class="specialty">Commercial and Industrial<br>property maintenance</p>
    <div class="rule rule--2"></div>
    <h2 class="heading heading--services">Services include</h2>
    <div class="rule rule--3"></div>

    <ul class="services-list services-list--left">
      <li class="service">Landscaping snow</li>
      <li class="service">Ice management</li>
      <li class="service">Janitorial services</li>
    </ul>
    <ul class="services-list services-list--right">
      <li class="service">Cleanroom services</li>
      <li class="service">Parking lot maintenance</li>
    </ul>

    <div class="card__band card__band--navy-top"></div>
    <div class="card__band card__band--gold"></div>
    <div class="card__band card__band--navy-bottom"></div>
  </main>
</body>
</html>
```